Banner Ad for Resume Services Website

The add is for this web site: www.BrightFolioDesk.com

The site offers 4 different services:

- Resume Writing (by a Certified Professional Resume Writer)
- Resume Posting (posts your resume to 85 job sites)
- Resume Distribution (sends your resume to hundreds of recruiters)
- Resume Online website (created an online resume with a domain name to your name)

Colors to be used are Blue, Yellow, etc... please check the website for inspiration.

Check the web site to learn more.

Target Market(s)

Unemployed, Professionals who want to switch jobs, etc..

Industry/Entity Type

Learn

Requirements
Must have
• We definitely one this to be included on the banner:

"Free Resume Samples"

in order to attract clicks.
Nice to have
• Some of the words we suggest to include on the banner are:

"How Good is Your Resume? Ask a Professional !"

Should not have
• No animation !

Do not place the LOGO on the banner as our LOGO might change in the near future. If you already submitted a banner with the LOGO on it, you can replace it with any other graphic that has a Resume/Jobs/BusinessStaff related theme.

```html
<!DOCTYPE html>
<html lang="en">
<head>
<meta charset="utf-8">
<title>Resume Services Banner</title>
<link href="https://fonts.googleapis.com/css2?family=Gentium+Book+Plus:ital,wght@0,400;0,700;1,400;1,700&family=Arimo:ital,wght@0,700;1,700&display=swap" rel="stylesheet">
<style>
  :root {
    --stage-top: #474747;
    --stage-bottom: #030303;
    --banner-light: #2f8fd8;
    --banner-mid: #1a6fc0;
    --banner-dark: #0f57a3;
    --banner-edge: #e8f2fb;
    --headline-green: #9ad14b;
    --service-white: #ffffff;
    --service-label: #dbe9f7;
    --ribbon-red: #cf3159;
    --ribbon-dark: #a8203f;
    --stitch: #f3a9bd;
    --paper-light: #f4f4f4;
    --paper-shade: #c9ced4;
  }
  * { margin: 0; padding: 0; box-sizing: border-box; }
  html, body {
    width: 1200px;
    height: 900px;
    overflow: hidden;
  }
  body {
    background: linear-gradient(to bottom, var(--stage-top) 0%, #1c1c1c 55%, var(--stage-bottom) 100%);
    position: relative;
    font-family: "Gentium Book Plus", Georgia, serif;
  }
  .banner {
    position: absolute;
    left: 62px;
    top: 380px;
    width: 1084px;
    height: 126px;
    border: 1.5px solid var(--banner-edge);
    border-radius: 6px;
    background:
      repeating-linear-gradient(115deg, rgba(255,255,255,0.035) 0 14px, rgba(255,255,255,0) 14px 40px),
      linear-gradient(160deg, var(--banner-light) 0%, var(--banner-mid) 50%, var(--banner-dark) 100%);
    overflow: hidden;
  }
  .resume-papers {
    position: absolute;
    left: 25px;
    top: 22px;
    width: 153px;
    height: 104px;
    background: linear-gradient(150deg, var(--paper-light) 0%, var(--paper-shade) 100%);
    border-radius: 2px 2px 0 0;
  }
  .headline {
    position: absolute;
    left: 199px;
    top: 10px;
    font-size: 39px;
    line-height: 1.1;
    font-weight: 700;
    color: var(--headline-green);
    white-space: nowrap;
  }
  .headline em { font-style: italic; }
  .headline .underlined {
    text-decoration: underline;
    text-decoration-thickness: 3px;
    text-underline-offset: 6px;
  }
  .services {
    position: absolute;
    left: 202px;
    top: 73px;
    display: flex;
    align-items: flex-end;
    gap: 15px;
    list-style: none;
    white-space: nowrap;
  }
  .service {
    display: flex;
    flex-direction: column;
    align-items: center;
    line-height: 1;
  }
  .service-label {
    font-style: italic;
    font-size: 15px;
    color: var(--service-label);
    margin-bottom: 4px;
  }
  .service-name {
    font-size: 21px;
    font-weight: 700;
    color: var(--service-white);
    letter-spacing: 0.3px;
  }
  .separator {
    color: var(--service-white);
    font-size: 18px;
    line-height: 1;
    padding-bottom: 2px;
  }
  .cta {
    position: absolute;
    left: 795px;
    top: 466px;
    width: 358px;
    height: 47px;
    text-decoration: none;
  }
  .cta svg { position: absolute; inset: 0; }
  .cta-text {
    position: absolute;
    left: 42px;
    top: 0;
    height: 47px;
    display: flex;
    align-items: center;
    font-family: "Arimo", Arial, sans-serif;
    font-weight: 700;
    font-size: 17px;
    color: #ffffff;
    white-space: nowrap;
    letter-spacing: 0.2px;
  }
  .cta-text em { font-style: italic; margin: 0 5px; }
  .cta-text .chevron { margin-left: 9px; font-size: 15px; }
</style>
</head>
<body>
  <section class="banner" aria-label="Resume services banner">
    <div class="resume-papers" role="img" aria-label="Stack of sample resume pages"></div>
    <h1 class="headline">Be Honest - <em>Just How Good</em> is <span class="underlined">your</span> Resume?</h1>
    <ul class="services">
      <li class="service"><span class="service-label">Resume</span><span class="service-name">Writing</span></li>
      <li class="separator">•</li>
      <li class="service"><span class="service-label">Resume</span><span class="service-name">Posting</span></li>
      <li class="separator">•</li>
      <li class="service"><span class="service-label">Resume</span><span class="service-name">Distribution</span></li>
      <li class="separator">•</li>
      <li class="service"><span class="service-label">Resume</span><span class="service-name">Websites</span></li>
    </ul>
  </section>

  <a class="cta" href="#">
    <svg width="358" height="47" viewBox="0 0 358 47" aria-hidden="true">
      <defs>
        <linearGradient id="ribbonFill" x1="0" y1="0" x2="0" y2="1">
          <stop offset="0" stop-color="#dd3c66"/>
          <stop offset="1" stop-color="#b92549"/>
        </linearGradient>
      </defs>
      <polygon points="0,0 358,0 358,47 0,47 14,23.5" fill="url(#ribbonFill)"/>
      <polyline points="6,4 354,4" fill="none" stroke="var(--stitch)" stroke-width="1" stroke-dasharray="3 3"/>
      <polyline points="6,43 354,43" fill="none" stroke="var(--stitch)" stroke-width="1" stroke-dasharray="3 3"/>
    </svg>
    <span class="cta-text">ACCESS<em>FREE</em>RESUME SAMPLES<span class="chevron">»</span></span>
  </a>
</body>
</html>
```